3D Printing Business coming soon page

Hi we are looking for a one page "coming soon" website for our business. The business is called "Solevia Labs" and it is a new solution which 3D Prints Orthotics (Insoles).

The design should include our logo, an improved version of our promotional image (attached), a web form for capturing interest from people, a countdown timer and some text.

Follow the colour scheme which is shown in our logo along with our other colours - Orange (RGB#ff8300) and Light Green (RGB#30f20a)
Updates

Industry/Entity Type

Business

Font styles to use
Sans Serif

Requirements
Must have
• Logo (Attached)
Improved version of Promotional Image
Web Form design for capturing Name, EMail Address and Comments along with a Turin test
Countdown Timer
Text - "Solevia Labs will shake up the Orthotics Industry. Foot Orthosis patient-ready in hours for a fraction of the price you are paying today. Welcome to the new world of 3D Printing!"

```html
<!DOCTYPE html>
<html lang="en">
<head>
<meta charset="utf-8">
<title>Solevia Labs – Coming Soon</title>
<link rel="stylesheet" href="https://fonts.googleapis.com/css2?family=Roboto+Condensed:ital,wght@0,300;0,400;0,700;1,700&family=Roboto:ital,wght@0,400;0,700;1,900&display=swap">
<style>
:root{
  --orange:#ff8300;
  --orange-light:#ffb347;
  --orange-pale:#ffe3b0;
  --green:#8dc63f;
  --green-bright:#6fd11a;
  --blue:#29a8e0;
  --black:#000;
  --grey-band:#666;
  --footer:#222;
  --step-text:#7a7a7a;
  --stripe:#d3eef2;
  --white:#fff;
  --timer-bg:#333;
  --timer-tile:#1c1c1c;
}
*{box-sizing:border-box;margin:0;padding:0}
html,body{width:1200px;height:950px;overflow:hidden}
body{position:relative;font-family:"Roboto Condensed",Arial,sans-serif;background:var(--white)}
.abs{position:absolute}

/* header */
.site-header{left:0;top:0;width:1200px;height:106px;background:var(--orange)}
.zigzag{left:0;top:100px;width:1200px;height:8px}
.brand{left:232px;top:18px;font-size:62px;font-weight:400;color:var(--white);line-height:78px;letter-spacing:-1px}
.call-tab{background:var(--blue);color:var(--white);font-family:Arial,sans-serif;font-size:11px;line-height:14px;padding:0 10px 0 22px;clip-path:polygon(12px 0,100% 0,100% 100%,0 100%)}
.phone{color:var(--white);font-family:Arial,sans-serif;font-size:28px;letter-spacing:1px;line-height:30px}

/* welcome band */
.welcome-band{left:0;top:106px;width:1200px;height:87px;background:var(--black)}
.welcome{left:200px;width:505px;text-align:center}
.welcome-line{top:118px;color:var(--white);font-size:29px;font-weight:300;line-height:34px}
.welcome-hero{top:148px;color:var(--green);font-size:38px;font-weight:700;line-height:40px}

/* stage */
.stage{left:0;top:193px;width:1200px;height:550px;
  background:
    linear-gradient(to bottom,rgba(255,255,255,0) 0%,rgba(255,255,255,.35) 50%,rgba(255,255,255,.95) 100%),
    repeating-linear-gradient(90deg,var(--stripe) 0 26px,#eaf7f9 26px 38px,#f3fbfc 38px 56px);}

.step-line{left:0;top:0;width:720px;height:743px}
.step-photo{width:114px;height:114px;border-radius:50%;border:5px solid var(--green);background:var(--white);overflow:hidden}
.step-photo span{display:block;width:100%;height:100%}
.step-label{color:var(--step-text);font-size:28px;font-weight:400;line-height:32px}

/* form */
.signup{left:723px;top:138px;width:247px;height:510px;border-radius:5px;border:1px solid #e07000;
  background:linear-gradient(to bottom,var(--orange-light) 0%,#ffa02a 45%,var(--orange) 100%)}
.signup-head{left:10px;top:9px;width:227px;height:56px;border-radius:8px 8px 0 0;
  background:linear-gradient(to bottom,#fff3d6,var(--orange-light));
  font-family:Roboto,sans-serif;font-style:italic;font-weight:900;font-size:25px;color:#111;text-align:center;line-height:74px}
.hurry{left:707px;top:202px;width:279px;height:72px;background:linear-gradient(to bottom,#a6e03a,var(--green-bright));
  transform:rotate(-2deg);box-shadow:0 2px 3px rgba(0,0,0,.25);text-align:center;color:var(--white);font-family:Roboto,sans-serif;font-style:italic}
.hurry strong{display:block;font-size:19px;font-weight:900;margin-top:10px;letter-spacing:.5px}
.hurry small{display:block;font-size:9.5px;font-weight:700;line-height:11px;padding:0 34px}
.field-label{width:80px;left:727px;text-align:right;font-family:Arial,sans-serif;font-size:11px;color:#111}
.field{left:817px;width:138px;background:var(--white);border:1px solid #f0c080}
.captcha{left:817px;top:479px;width:138px;height:26px;background:var(--white);font-family:"Roboto Condensed",sans-serif;font-weight:700;font-size:15px;line-height:26px;text-align:center;color:#111;letter-spacing:.5px}
.captcha-hint{left:818px;top:514px;font-family:Arial,sans-serif;font-size:11px;color:#111}
.captcha-tools{left:941px;top:533px;width:14px;height:29px;background:#f4f4f4}
.submit{left:775px;top:598px;width:151px;height:42px;border-radius:8px;border:1px solid #e68a00;
  background:linear-gradient(to bottom,#ffe19a,#ffb02e 55%,#ff9a00);
  font-family:Roboto,sans-serif;font-style:italic;font-weight:900;font-size:21px;color:#222;text-align:center;line-height:42px}

/* countdown */
.countdown{left:723px;top:651px;width:246px;height:76px;background:var(--timer-bg);border-radius:4px;display:flex;padding:6px 6px 0;gap:0}
.unit{width:58.5px;text-align:center;color:var(--white)}
.digits{display:block;margin:0 3px;height:45px;background:linear-gradient(to bottom,#2a2a2a 50%,#151515 50%);border-radius:3px;font-size:40px;line-height:46px;font-weight:400}
.unit-name{display:block;font-size:12px;margin-top:5px}
.colon{left:0;color:var(--white);font-size:30px}

/* bottom */
.pitch{left:0;top:743px;width:1200px;height:72px;background:var(--grey-band);color:var(--white);font-size:17.5px;line-height:24px;text-align:center;padding-top:13px}
.site-footer{left:0;top:815px;width:1200px;height:135px;background:var(--footer)}
.footer-brand{left:790px;top:842px;width:180px;text-align:right;font-size:33px;color:var(--white);line-height:44px;letter-spacing:-1px}
</style>
</head>
<body>

<header class="site-header abs"></header>
<svg class="zigzag abs" viewBox="0 0 1200 8" preserveAspectRatio="none" aria-hidden="true">
  <polygon fill="#ff8300" points="0,0 1200,0 1200,2 1194,6 1188,2 1182,6 1176,2 1170,6 1164,2 1158,6 1152,2 1146,6 1140,2 1134,6 1128,2 1122,6 1116,2 1110,6 1104,2 1098,6 1092,2 1086,6 1080,2 1074,6 1068,2 1062,6 1056,2 1050,6 1044,2 1038,6 1032,2 1026,6 1020,2 1014,6 1008,2 1002,6 996,2 990,6 984,2 978,6 972,2 966,6 960,2 954,6 948,2 942,6 936,2 930,6 924,2 918,6 912,2 906,6 900,2 894,6 888,2 882,6 876,2 870,6 864,2 858,6 852,2 846,6 840,2 834,6 828,2 822,6 816,2 810,6 804,2 798,6 792,2 786,6 780,2 774,6 768,2 762,6 756,2 750,6 744,2 738,6 732,2 726,6 720,2 714,6 708,2 702,6 696,2 690,6 684,2 678,6 672,2 666,6 660,2 654,6 648,2 642,6 636,2 630,6 624,2 618,6 612,2 606,6 600,2 594,6 588,2 582,6 576,2 570,6 564,2 558,6 552,2 546,6 540,2 534,6 528,2 522,6 516,2 510,6 504,2 498,6 492,2 486,6 480,2 474,6 468,2 462,6 456,2 450,6 444,2 438,6 432,2 426,6 420,2 414,6 408,2 402,6 396,2 390,6 384,2 378,6 372,2 366,6 360,2 354,6 348,2 342,6 336,2 330,6 324,2 318,6 312,2 306,6 300,2 294,6 288,2 282,6 276,2 270,6 264,2 258,6 252,2 246,6 240,2 234,6 228,2 222,6 216,2 210,6 204,2 198,6 192,2 186,6 180,2 174,6 168,2 162,6 156,2 150,6 144,2 138,6 132,2 126,6 120,2 114,6 108,2 102,6 96,2 90,6 84,2 78,6 72,2 66,6 60,2 54,6 48,2 42,6 36,2 30,6 24,2 18,6 12,2 6,6 0,2"/>
</svg>
<div class="brand abs">Solevia Labs</div>
<div class="call-tab abs" style="left:860px;top:32px;width:118px">Call us to Join</div>
<div class="phone abs" style="left:776px;top:48px">+888 410 2736</div>

<section class="welcome-band abs"></section>
<h1 class="welcome welcome-line abs">WELCOME TO THE NEW WORLD OF</h1>
<h2 class="welcome welcome-hero abs">3D PRINTING!</h2>

<div class="stage abs"></div>

<svg class="step-line abs" viewBox="0 0 720 743" aria-hidden="true">
  <polyline points="327,264 396,380 304,495 383,609" fill="none" stroke="#8dc63f" stroke-width="6"/>
</svg>

<div class="step-photo abs" style="left:270px;top:207px"><span role="img" aria-label="Laptop showing a foot pressure scan" style="background:linear-gradient(135deg,#dfe6ee,#3b4d7a 55%,#222)"></span></div>
<div class="step-photo abs" style="left:339px;top:323px"><span role="img" aria-label="Foot resting on a custom orthotic insole" style="background:linear-gradient(160deg,#f3ede6,#e3cdb5 55%,#cbb7a0)"></span></div>
<div class="step-photo abs" style="left:247px;top:438px"><span role="img" aria-label="Desktop 3D printer" style="background:linear-gradient(150deg,#f2f2f2,#c7b0bc 50%,#8a2a45)"></span></div>
<div class="step-photo abs" style="left:326px;top:552px"><span role="img" aria-label="Hand fitting a printed insole into a shoe" style="background:linear-gradient(150deg,#eeeeee,#d9c1a3 50%,#2a2a2a)"></span></div>

<div class="step-label abs" style="left:400px;top:229px">1. Scan the foot</div>
<div class="step-label abs" style="left:459px;top:359px">2. Design the Orthotic</div>
<div class="step-label abs" style="left:370px;top:481px">3. 3D Print It</div>
<div class="step-label abs" style="left:449px;top:597px">4. Fit It</div>

<form class="signup abs" aria-label="Early access registration">
  <div class="signup-head abs">Get Started Now !</div>
</form>
<div class="hurry abs"><strong>HURRY !</strong><small>Register now during this special pre-launch invitation and get early access!</small></div>

<label class="field-label abs" style="top:286px">First Name</label>
<div class="field abs" style="top:285px;height:16px"></div>
<label class="field-label abs" style="top:311px">Last Name</label>
<div class="field abs" style="top:309px;height:16px"></div>
<label class="field-label abs" style="top:336px">E-mail Address</label>
<div class="field abs" style="top:334px;height:16px"></div>
<label class="field-label abs" style="top:361px">Message</label>
<div class="field abs" style="top:359px;height:109px"></div>
<div class="captcha abs">poration submits</div>
<div class="captcha-hint abs">Type the above words:</div>
<div class="field abs" style="top:533px;height:29px"></div>
<svg class="captcha-tools abs" viewBox="0 0 14 29" aria-hidden="true">
  <circle cx="7" cy="6" r="3" fill="none" stroke="#d33" stroke-width="1.5"/>
  <polygon points="4,13 7,13 10,10 10,19 7,16 4,16" fill="#d33"/>
  <circle cx="7" cy="24" r="3" fill="#d33"/>
</svg>
<div class="submit abs">SUBMIT</div>

<div class="countdown abs" role="timer" aria-label="Launch countdown">
  <div class="unit"><span class="digits">01</span><span class="unit-name">DAYS</span></div>
  <div class="unit"><span class="digits">06</span><span class="unit-name">HRS</span></div>
  <div class="unit"><span class="digits">35</span><span class="unit-name">MINS</span></div>
  <div class="unit"><span class="digits">48</span><span class="unit-name">SECS</span></div>
</div>
<div class="colon abs" style="left:783px;top:663px">:</div>
<div class="colon abs" style="left:841px;top:663px">:</div>
<div class="colon abs" style="left:900px;top:663px">:</div>

<p class="pitch abs">Solevia Labs will shake up the Orthotics Industry. Foot Orthosis patient-ready in hours for a fraction of the<br>price you are paying today. Welcome to the new world of 3D Printing!</p>

<footer class="site-footer abs"></footer>
<div class="footer-brand abs">Solevia Labs</div>
<div class="call-tab abs" style="left:848px;top:887px;width:117px">Call us to Join</div>
<div class="phone abs" style="left:762px;top:903px">+888 410 2736</div>

</body>
</html>
```